Business Card for Consulting Company

I would need a business card for my consulting company - the company brand and logos are defined and shared as part of this project. The proposed design for the business card can be reused as inspiration for my email signature.

```html
<!DOCTYPE html>
<html lang="en">
<head>
<meta charset="utf-8">
<title>Halvern Consulting – Business Card</title>
<link href="https://fonts.googleapis.com/css2?family=Montserrat:wght@400;500;600;700&display=swap" rel="stylesheet">
<style>
  :root {
    --teal: #19abac;
    --ink: #3a3a3c;
    --paper: #ffffff;
    --backdrop-top: #d2d2d2;
    --backdrop-bottom: #a9a9a9;
  }
  * { margin: 0; padding: 0; box-sizing: border-box; }
  html, body { width: 1200px; height: 788px; overflow: hidden; }
  body {
    background: linear-gradient(180deg, var(--backdrop-top), var(--backdrop-bottom));
    font-family: "Montserrat", sans-serif;
    position: relative;
  }
  .card {
    position: absolute;
    width: 530px;
    height: 330px;
    border-radius: 22px;
    box-shadow: 0 14px 30px rgba(0,0,0,0.28);
    overflow: hidden;
  }
  .card--front { left: 50px; top: 140px; background: var(--paper); }
  .card--back  { left: 620px; top: 318px; background: var(--teal); }

  .brand {
    position: absolute;
    left: 0; right: 0; top: 70px;
    display: flex;
    align-items: center;
    justify-content: center;
    gap: 12px;
  }
  .brand__dot {
    width: 22px; height: 22px;
    border-radius: 50%;
    background: var(--teal);
  }
  .brand__name {
    font-weight: 700;
    font-size: 40px;
    letter-spacing: 1px;
    color: var(--teal);
  }

  .details {
    position: absolute;
    left: 40px; right: 30px; bottom: 52px;
    display: flex;
    align-items: center;
  }
  .person { flex: 0 0 auto; padding-right: 22px; text-align: right; }
  .person__name {
    font-weight: 600;
    font-size: 21px;
    letter-spacing: 1px;
    text-transform: uppercase;
    color: var(--teal);
  }
  .person__role {
    font-weight: 400;
    font-size: 15px;
    color: var(--ink);
    margin-top: 2px;
  }
  .divider {
    width: 1px; height: 66px;
    background: var(--teal);
  }
  .contact { list-style: none; padding-left: 22px; }
  .contact__item {
    display: flex;
    align-items: center;
    gap: 8px;
    font-size: 14px;
    color: var(--ink);
    line-height: 22px;
  }
  .contact__icon { width: 12px; height: 12px; flex: 0 0 12px; }

  .back-brand {
    position: absolute;
    inset: 0;
    display: flex;
    align-items: center;
    justify-content: center;
    gap: 16px;
  }
  .back-brand__dot {
    width: 34px; height: 34px;
    border-radius: 50%;
    background: var(--paper);
  }
  .back-brand__name {
    font-weight: 700;
    font-size: 52px;
    letter-spacing: 1px;
    color: var(--paper);
  }
</style>
</head>
<body>
  <section class="card card--front" aria-label="Business card front">
    <div class="brand">
      <span class="brand__dot"></span>
      <span class="brand__name">Halvern</span>
    </div>

    <div class="details">
      <div class="person">
        <p class="person__name">Mathis Arnaud</p>
        <p class="person__role">Founder &amp; CEO</p>
      </div>
      <span class="divider"></span>
      <ul class="contact">
        <li class="contact__item">
          <svg class="contact__icon" viewBox="0 0 12 12" aria-hidden="true">
            <path fill="#19abac" d="M2.3 0.8l2 2-1 1.4c.7 1.6 1.9 2.8 3.5 3.5l1.4-1 2 2-1.2 1.8C5 10.2 1.8 7 .5 2z"/>
          </svg>
          +41 79 000 12 34
        </li>
        <li class="contact__item">
          <svg class="contact__icon" viewBox="0 0 12 12" aria-hidden="true">
            <rect x="0.5" y="2" width="11" height="8" rx="1" fill="#19abac"/>
            <path d="M1 2.7l5 3.8 5-3.8" fill="none" stroke="#fff" stroke-width="1"/>
          </svg>
          mathis.a@halvern.ch
        </li>
        <li class="contact__item">
          <svg class="contact__icon" viewBox="0 0 12 12" aria-hidden="true">
            <circle cx="6" cy="6" r="5.5" fill="#19abac"/>
            <path d="M1 6h10M6 .8c-2.4 2.9-2.4 7.5 0 10.4M6 .8c2.4 2.9 2.4 7.5 0 10.4" fill="none" stroke="#fff" stroke-width=".8"/>
          </svg>
          www.halvern.ch
        </li>
      </ul>
    </div>
  </section>

  <section class="card card--back" aria-label="Business card back">
    <div class="back-brand">
      <span class="back-brand__dot"></span>
      <span class="back-brand__name">Halvern</span>
    </div>
  </section>
</body>
</html>
```